Birchfield Dental Care Stationery

create stationery, business cards and envelops for business. Use current logo on website but open to new fonts for the business name. Business name is Birchfield Dental Care, would like below the name added "Cosmetic - Family - Implants" Website is www.birchfielddentalcareQX.example. I would like to have modern look, clean, and professional. The water mark of the logo is a great thing to ad as well.

Target Market(s)

General public, Families, Cosmetic, Implant

Industry/Entity Type

Dental

Font styles to use
Sans Serif

Colors
9bcb3c
000000
757575
c9c9c9

Requirements
Must have
• Would like to see different versions of the current logo. Improvements, color, sytle, and class.
Nice to have
• current font has double "oo" in the Birchfield logo, does not need to have with new logo.

```html
<!DOCTYPE html>
<html lang="en">
<head>
<meta charset="utf-8">
<title>Birchfield Dental Care Stationery</title>
<link href="https://fonts.googleapis.com/css2?family=PT+Sans:wght@400;700&family=PT+Sans+Narrow:wght@400;700&display=swap" rel="stylesheet">
<style>
  :root {
    --bg: #bfe2ee;
    --paper: #ffffff;
    --paper-shade: #f1f3f5;
    --teal-dark: #0d5a78;
    --teal: #1a7fa3;
    --sky: #5fc0e8;
    --text: #4a4f55;
    --muted: #757575;
    --line: #c9c9c9;
    --mark: #e4ebef;
  }
  * { box-sizing: border-box; margin: 0; padding: 0; }
  html, body { width: 1200px; height: 960px; overflow: hidden; }
  body {
    background: var(--bg);
    font-family: "PT Sans Narrow", "Arial Narrow", sans-serif;
    color: var(--text);
    position: relative;
  }
  .sheet { position: absolute; background: var(--paper); box-shadow: 0 6px 18px rgba(20,80,110,.18); overflow: hidden; }

  /* brand */
  .brand { display: flex; align-items: center; gap: 8px; }
  .brand-dot { width: 26px; height: 26px; border: 3px solid var(--teal); border-radius: 50%; flex: none; }
  .brand-name { font-family: "PT Sans", sans-serif; font-weight: 700; color: var(--teal); font-size: 19px; line-height: 1; white-space: nowrap; }
  .brand-tagline { font-size: 11px; color: var(--sky); letter-spacing: .3px; margin-top: 4px; border-top: 1px solid var(--teal); padding-top: 3px; white-space: nowrap; }

  .icon { width: 11px; height: 11px; flex: none; }

  .watermark { position: absolute; border: 14px solid var(--mark); border-radius: 50%; }

  /* letterhead */
  .letterhead { left: 40px; top: 40px; width: 500px; height: 679px; }
  .letterhead .brand-block { position: absolute; left: 34px; top: 34px; }
  .letterhead .contact { position: absolute; right: 30px; top: 120px; font-size: 10px; line-height: 1.5; }
  .contact-row { display: flex; align-items: center; gap: 5px; white-space: nowrap; }
  .letterhead .watermark { width: 250px; height: 250px; left: 125px; top: 195px; }

  .services-tab { position: absolute; left: 24px; top: 470px; background: var(--sky); color: #fff; font-size: 12px; padding: 2px 16px; }
  .services-rule { position: absolute; left: 24px; right: 130px; top: 489px; height: 1px; background: var(--teal); }
  .services { position: absolute; left: 24px; right: 20px; top: 498px; display: flex; justify-content: space-between; }
  .services ul { list-style: none; font-size: 8px; line-height: 1.35; white-space: nowrap; }
  .services ul:nth-child(2) { margin-top: 6px; }
  .services ul:nth-child(3) { margin-top: 12px; }
  .services ul:nth-child(4) { margin-top: 18px; }
  .services ul:nth-child(5) { margin-top: 24px; }
  .services li::before { content: "▸ "; color: var(--teal); }
  .hours { position: absolute; right: 24px; top: 598px; font-size: 8px; line-height: 1.4; text-align: right; color: var(--text); white-space: nowrap; }

  .foot-bar { position: absolute; left: 0; right: 0; bottom: 0; height: 30px; background: linear-gradient(90deg, var(--teal-dark), var(--teal) 60%, var(--sky)); border-top: 3px solid var(--line); display: flex; align-items: center; justify-content: flex-end; padding-right: 20px; gap: 6px; color: #fff; font-size: 12px; }

  /* business cards */
  .card { width: 340px; height: 190px; }
  .card-front { left: 580px; top: 60px; background: var(--teal-dark); display: flex; align-items: center; justify-content: center; }
  .card-front .brand-name { color: #fff; }
  .card-front .brand-dot { border-color: #fff; }
  .card-front .brand-tagline { color: #cfe9f3; border-top-color: #fff; text-align: center; }

  .card-back { left: 580px; top: 290px; display: flex; align-items: center; padding: 0 14px; border-bottom: 5px solid var(--teal); }
  .card-back .brand-name { font-size: 12px; }
  .card-back .brand-dot { width: 18px; height: 18px; border-width: 2px; }
  .card-back .brand-tagline { font-size: 8.5px; }
  .card-divider { width: 1px; height: 90px; background: var(--line); margin: 0 8px; flex: none; }
  .card-details { font-size: 8px; line-height: 1.55; }
  .card-details .icon { width: 9px; height: 9px; }
  .card-person { font-family: "PT Sans", sans-serif; font-weight: 700; color: var(--teal-dark); font-size: 10px; margin-bottom: 4px; white-space: nowrap; }

  /* envelope */
  .envelope { left: 560px; top: 530px; width: 610px; height: 310px; background: linear-gradient(180deg, var(--paper), var(--paper-shade)); }
  .envelope .brand-block { position: absolute; left: 34px; top: 30px; }
  .envelope .watermark { width: 170px; height: 170px; right: 40px; top: 90px; border-width: 10px; }
  .envelope .address { position: absolute; left: 34px; bottom: 52px; display: flex; gap: 14px; font-size: 13px; color: var(--muted); white-space: nowrap; }
  .envelope .address span { display: flex; align-items: center; gap: 5px; }
  .envelope .icon { width: 13px; height: 13px; }
</style>
</head>
<body>

<svg width="0" height="0" style="position:absolute">
  <defs>
    <symbol id="ico-pin" viewBox="0 0 12 12"><circle cx="6" cy="6" r="5.3" fill="none" stroke="currentColor"/><path d="M6 2.5a2 2 0 0 1 2 2c0 1.5-2 4-2 4s-2-2.5-2-4a2 2 0 0 1 2-2z" fill="currentColor"/></symbol>
    <symbol id="ico-phone" viewBox="0 0 12 12"><circle cx="6" cy="6" r="5.3" fill="none" stroke="currentColor"/><path d="M4 3l1.2 1.3-.6.8c.4.9 1 1.5 1.9 1.9l.8-.6L8.6 7.6 8 8.8C5.5 8.6 3.4 6.5 3.2 4z" fill="currentColor"/></symbol>
    <symbol id="ico-fax" viewBox="0 0 12 12"><circle cx="6" cy="6" r="5.3" fill="none" stroke="currentColor"/><rect x="3.5" y="5" width="5" height="3" fill="currentColor"/><rect x="4.5" y="3" width="3" height="2" fill="none" stroke="currentColor" stroke-width=".7"/></symbol>
    <symbol id="ico-globe" viewBox="0 0 12 12"><circle cx="6" cy="6" r="5" fill="none" stroke="currentColor"/><ellipse cx="6" cy="6" rx="2" ry="5" fill="none" stroke="currentColor" stroke-width=".7"/><path d="M1 6h10" stroke="currentColor" stroke-width=".7"/></symbol>
  </defs>
</svg>

<!-- Letterhead -->
<section class="sheet letterhead">
  <div class="brand-block">
    <div class="brand"><span class="brand-dot"></span><span class="brand-name">Birchfield Dental Care</span></div>
    <div class="brand-tagline">Cosmetic • Family • Implants</div>
  </div>
  <div class="contact">
    <div class="contact-row"><svg class="icon"><use href="#ico-pin"/></svg>218 North Alder Lane, Fenwick, QX 40517</div>
    <div class="contact-row"><svg class="icon"><use href="#ico-phone"/></svg>(555) 010-4821 <svg class="icon"><use href="#ico-fax"/></svg>(555) 010-4836</div>
    <div class="contact-row">Provider No. 000000W &nbsp;|&nbsp; ABN 00 000 000 069</div>
  </div>
  <div class="watermark" aria-hidden="true"></div>

  <div class="services-tab">Services</div>
  <div class="services-rule"></div>
  <div class="services">
    <ul><li>Bonding</li><li>Cosmetic Contouring</li><li>Crowns and Bridges</li><li>Specialty Dentures</li><li>Cosmetic Fillings</li><li>Implants</li></ul>
    <ul><li>Veneers</li><li>Teeth Whitening</li><li>Bone Grafting</li><li>Excessive or Uneven Gums</li><li>Jaw/TMJ</li><li>Nitrous Oxide Sedation</li></ul>
    <ul><li>Oral Sedation</li><li>Sealants</li><li>Root Canal Therapy</li><li>Extractions</li><li>Scaling and Root Planing</li><li>Implant Retained Dentures</li></ul>
    <ul><li>Cosmetic Dentistry</li><li>Sleep Apnea Treatment</li><li>Snoring Treatment</li><li>Maxillofacial Surgery</li><li>Laser Dentistry</li><li>Laser Surgery</li></ul>
    <ul><li>Digital X-rays</li><li>Intra Oral Photography</li><li>Dental Implants</li><li>Implant Supported Dentures</li><li>Oral Surgery</li></ul>
  </div>
  <div class="hours">
    Monday: 08:00 AM - 04:00 PM | Tuesday: 08:00 AM - 04:00 PM<br>
    Wednesday: By Appointment Only | Thursday: 08:00 AM - 04:00 PM<br>
    Friday: 08:00 AM - 03:00 PM | Saturday: Available by appointment<br>
    Sunday: Closed
  </div>
  <div class="foot-bar"><svg class="icon"><use href="#ico-globe"/></svg>www.birchfielddentalcareQX.example</div>
</section>

<!-- Business card front -->
<section class="sheet card card-front">
  <div>
    <div class="brand"><span class="brand-dot"></span><span class="brand-name">Birchfield Dental Care</span></div>
    <div class="brand-tagline">Cosmetic - Family - Implants</div>
  </div>
</section>

<!-- Business card back -->
<section class="sheet card card-back">
  <div>
    <div class="brand"><span class="brand-dot"></span><span class="brand-name">Birchfield Dental Care</span></div>
    <div class="brand-tagline">Cosmetic • Family • Implants</div>
  </div>
  <div class="card-divider"></div>
  <div class="card-details">
    <div class="card-person">Dr. Martin L. Osric D.D.S.</div>
    <div class="contact-row"><svg class="icon"><use href="#ico-pin"/></svg>218 North Alder Lane,</div>
    <div class="contact-row" style="padding-left:14px">Fenwick, QX 40517</div>
    <div class="contact-row"><svg class="icon"><use href="#ico-phone"/></svg>(555) 010-4821</div>
    <div class="contact-row"><svg class="icon"><use href="#ico-fax"/></svg>(555) 010-4836</div>
    <div class="contact-row"><svg class="icon"><use href="#ico-globe"/></svg>www.birchfielddentalcareQX.example</div>
  </div>
</section>

<!-- Envelope -->
<section class="sheet envelope">
  <div class="brand-block">
    <div class="brand"><span class="brand-dot"></span><span class="brand-name">Birchfield Dental Care</span></div>
    <div class="brand-tagline">Cosmetic • Family • Implants</div>
  </div>
  <div class="watermark" aria-hidden="true"></div>
  <div class="address">
    <span><svg class="icon"><use href="#ico-pin"/></svg>218 North Alder Lane, Fenwick, QX 40517</span>
    <span><svg class="icon"><use href="#ico-phone"/></svg>(555) 010-4821</span>
    <span><svg class="icon"><use href="#ico-fax"/></svg>(555) 010-4836</span>
  </div>
  <div class="foot-bar"><svg class="icon"><use href="#ico-globe"/></svg>www.birchfielddentalcareQX.example</div>
</section>

</body>
</html>
```